PSD website for property company

Please read the brief thoroughly.

We are looking for a new website for a property group that does property acquisitions, property development and property management.
They buy, build and lease core inner city industrial assets in Sydney, Australia.
They also invest in residential developments.

Site menu
- Home page
- Property – sub menus include – Leasing ; Projects ; Investments ; Property Management
- Capital and finance
- About
- Contact

They like this website
https://www.verlo.com.au/

They want the site to be clean, modern and bold.
They like few colors, even black and white is OK to submit

They have a logo and style guide and useable images here:
http://www.kumet.net/temp/PelorisWeb2019.zip
The zip file is also attached to this project.
We have supplied some images to give you an idea, but we will also require you to provide at least 3 extra images from stock photos.
Use your imagination.

I am expecting a lot of similar designs, so be aware the photos you choose will be really important.
They want really 3 good stock photos used and supplied without charge.
Please not too generic, I repeat the quality of the photos is important.
You may provide several photos (but not in multiple submissions please) and we will choose the best three to be provided.

The winner will be selected on a single home page design and required to provide;
All photos use in original format without charge
A second ‘standard page’ template design based on the winning home page design

```html
<!DOCTYPE html>
<html lang="en">
<head>
<meta charset="utf-8">
<title>Peloris — Property Group</title>
<link href="https://fonts.googleapis.com/css2?family=Open+Sans:wght@400;600;700&display=swap" rel="stylesheet">
<style>
:root{
  --ink:#111;
  --topbar:#0f1a0b;
  --olive:#5b6d35;
  --olive-btn:#56702e;
  --accent:#f0c419;
  --paper:#f2f2f2;
  --stone:#dcdcdc;
  --footer:#242424;
  --white:#fff;
  --sky:#b7cde3;
  --sky-deep:#7fa3d1;
  --brick:#6e4a36;
  --brick-dark:#4a3329;
  --glass:#4f74a8;
  --leaf:#4f6b33;
  --street:#2e2a27;
}
*{margin:0;padding:0;box-sizing:border-box}
html,body{width:1200px;height:3719px;overflow:hidden}
body{position:relative;font-family:"Open Sans",Arial,sans-serif;color:var(--ink);background:var(--paper)}
.abs{position:absolute}
a{color:inherit;text-decoration:none}

/* header */
.topbar{left:0;top:0;width:1200px;height:33px;background:var(--topbar);color:var(--white);font-size:17px}
.topbar .phone{position:absolute;left:940px;top:5px;display:flex;align-items:center;gap:6px}
.topbar .social{position:absolute;left:1131px;top:7px;width:19px;height:19px;background:#3b5a9a}
.navbar{left:0;top:33px;width:1200px;height:80px;background:var(--olive)}
.brand{position:absolute;left:23px;top:16px;font-weight:600;font-size:42px;letter-spacing:6px;color:var(--white);line-height:48px}
.menu{position:absolute;top:31px;font-size:16px;font-weight:600;color:var(--white);text-transform:uppercase}
.menu.active{color:var(--accent)}
.dropdown{left:530px;top:113px;width:293px;height:176px;background:rgba(30,30,30,.88);z-index:3}
.dropdown li{list-style:none;position:absolute;left:29px;color:var(--white);font-size:21px}

/* photo areas: soft gradients in each scene's main tones */
.photo-hero{background:
  radial-gradient(ellipse 260px 200px at 1040px 330px,rgba(79,107,51,.75),transparent 70%),
  radial-gradient(ellipse 240px 180px at 420px 360px,rgba(79,107,51,.6),transparent 70%),
  linear-gradient(180deg,#c9d9e8 0%,#b3c7da 14%,#8a6a55 30%,var(--brick) 52%,#5b4436 74%,var(--street) 100%)}
.photo-brick{background:
  radial-gradient(ellipse 300px 260px at 380px 230px,rgba(74,51,41,.9),transparent 75%),
  linear-gradient(180deg,#cfdceb 0%,#b9cde0 30%,#8b7a70 55%,#4a3a32 100%)}
.photo-white{background:
  radial-gradient(ellipse 260px 120px at 200px 330px,rgba(79,107,51,.7),transparent 75%),
  linear-gradient(180deg,#a9c4e2 0%,#c5d6e8 35%,#d8d6d0 52%,#a7a39b 72%,#5e6b4f 100%)}
.photo-tower{background:
  radial-gradient(ellipse 170px 300px at 250px 200px,rgba(60,95,150,.85),transparent 75%),
  linear-gradient(170deg,var(--sky-deep) 0%,#a9c1dc 40%,#8a8f96 70%,#2f3338 100%)}
.photo-campus{background:
  radial-gradient(ellipse 170px 220px at 500px 170px,rgba(70,110,50,.85),transparent 75%),
  radial-gradient(ellipse 280px 150px at 260px 200px,rgba(79,116,168,.85),transparent 75%),
  linear-gradient(180deg,#7fa8dc 0%,#b5cce6 30%,#8fa2b6 55%,#5f8a42 80%,#b9b2a2 100%)}
.photo-thin-glass{background:linear-gradient(180deg,#c2a36d 0%,#8a8a86 45%,#4d5a66 100%)}
.photo-thin-brick{background:linear-gradient(180deg,#bccde0 0%,#7b5b48 40%,#4a3329 100%)}
.photo-dusk{background:
  radial-gradient(ellipse 130px 330px at 880px 220px,rgba(60,80,115,.85),transparent 75%),
  radial-gradient(ellipse 120px 240px at 1000px 310px,rgba(170,150,120,.6),transparent 75%),
  radial-gradient(ellipse 700px 120px at 800px 520px,rgba(40,60,30,.9),transparent 75%),
  linear-gradient(180deg,#86a9d8 0%,#b1c6dd 40%,#7d8b95 68%,#2f3a2c 100%)}

/* hero */
.hero{left:0;top:113px;width:1200px;height:527px}
.hero-title{left:0;top:246px;width:1200px;text-align:center;font-size:80px;font-weight:600;color:var(--white);line-height:100px;letter-spacing:1px}
.hero-caption{left:0;top:530px;width:1200px;height:62px;background:rgba(40,40,40,.6);color:var(--white);font-size:19px;text-align:center;line-height:62px}
.dot{top:608px;width:20px;height:20px;border-radius:50%;background:var(--white)}
.dot.on{background:var(--olive-btn);border:2px solid var(--white)}

/* welcome */
.welcome-title{left:0;top:695px;width:1200px;text-align:center;font-size:44px;font-weight:700}
.welcome-text{left:148px;top:791px;width:904px;text-align:center;font-size:17.6px;line-height:24.5px;color:#333}

.card{top:1002px;width:588px;height:442px}
.card .shade{position:absolute;left:0;bottom:0;width:100%;height:130px;background:linear-gradient(180deg,rgba(30,30,30,.6),rgba(20,20,20,.88));color:var(--white)}
.card h3{position:absolute;left:23px;top:12px;font-size:23px;font-weight:700}
.card p{position:absolute;left:23px;top:44px;width:545px;font-size:13.4px;line-height:16px}
.btn-more{position:absolute;height:25px;width:115px;background:var(--olive-btn);border:1.5px solid var(--white);color:var(--white);font-size:13px;display:flex;align-items:center;justify-content:center;gap:8px}

/* management */
.stone{left:0;top:1571px;width:1200px;height:1300px;background:var(--stone)}
.mgmt-photo{left:520px;top:1606px;width:580px;height:453px}
.mgmt-box{left:98px;top:1677px;width:501px;height:274px;background:rgba(236,236,236,.88)}
.mgmt-box h3{position:absolute;left:42px;top:45px;font-size:23px;font-weight:700}
.mgmt-box p{position:absolute;left:42px;top:98px;width:325px;font-size:13.4px;line-height:16px;color:#222}

/* projects */
.rule{height:1px;background:#555}
.section-title{font-size:22px;font-weight:700;text-align:center}
.filter{font-weight:700}
.arrow{position:absolute}
.project-name{left:305px;top:2717px;font-size:23px;font-weight:700}
.project-text{left:305px;top:2756px;width:330px;font-size:13.4px;line-height:16px}

/* newsletter */
.keep{left:0;top:2871px;width:1200px;height:159px;background:var(--paper)}
.keep-sub{left:0;top:2950px;width:1200px;text-align:center;font-size:18px;color:#333}
.signup{left:0;top:3030px;width:1200px;height:566px}
.signup-panel{left:0;top:3097px;width:669px;height:499px;background:rgba(35,35,35,.78)}
.field{left:84px;width:421px;height:35px;border:1px solid #9a9a9a;color:#ddd;font-size:14px;padding-left:21px;line-height:33px}
.field b{color:#9bbd3a;font-weight:400}
.interest{left:84px;top:3328px;width:421px;text-align:center;color:var(--white);font-size:16px}
.chip{top:3375px;height:34px;border:1.5px solid #bbb;border-radius:5px;color:var(--white);font-size:14px;display:flex;align-items:center;justify-content:center}
.submit{left:94px;top:3438px;width:420px;height:35px;background:var(--olive-btn);border:1.5px solid #d8d8d8;border-radius:5px;color:var(--white);font-size:16px;display:flex;align-items:center;justify-content:center}

/* footer */
.footer{left:0;top:3596px;width:1200px;height:123px;background:var(--footer);color:var(--white)}
.footer-nav{position:absolute;top:22px;width:100%;display:flex;justify-content:center;gap:20px;font-size:15px}
.footer-nav span.sep{color:#aaa}
.copy{position:absolute;top:88px;width:100%;text-align:center;font-size:12px;color:#777}
</style>
</head>
<body>

<header>
  <div class="abs topbar">
    <span class="phone">
      <svg width="16" height="16" viewBox="0 0 24 24" fill="none" stroke="#fff" stroke-width="2"><path d="M5 3h4l2 5-3 2a11 11 0 0 0 6 6l2-3 5 2v4a2 2 0 0 1-2 2A17 17 0 0 1 3 5a2 2 0 0 1 2-2z"/></svg>
      02 8100 XXX
    </span>
    <span class="social" aria-label="Social link"></span>
  </div>
  <nav class="abs navbar">
    <a class="brand" href="#">PELORIS</a>
    <a class="menu" style="left:445px">Home</a>
    <a class="menu active" style="left:563px">Property</a>
    <a class="menu" style="left:712px">Capital and Finance</a>
    <a class="menu" style="left:953px">About</a>
    <a class="menu" style="left:1079px">Contact</a>
  </nav>
  <ul class="abs dropdown">
    <li style="top:9px">Leasing</li>
    <li style="top:52px">Projects</li>
    <li style="top:95px">Investments</li>
    <li style="top:138px">Property Management</li>
  </ul>
</header>

<section>
  <div class="abs hero photo-hero" role="img" aria-label="Brick apartment building with arched windows and street trees"></div>
  <h1 class="abs hero-title">LOREM IPSUM</h1>
  <svg class="arrow" style="left:44px;top:308px" width="44" height="72" viewBox="0 0 44 72"><path d="M38 4 8 36l30 32" fill="none" stroke="#fff" stroke-width="8"/></svg>
  <svg class="arrow" style="left:1133px;top:308px" width="44" height="72" viewBox="0 0 44 72"><path d="M6 4l30 32L6 68" fill="none" stroke="#fff" stroke-width="8"/></svg>
  <p class="abs hero-caption">Lorem ipsum dolor sit amet, consectetur adipiscing elit, sed do eiusmod tempor incididunt ut labore et dolore magna aliqua.</p>
  <span class="abs dot on" style="left:543px"></span>
  <span class="abs dot" style="left:573px"></span>
  <span class="abs dot" style="left:605px"></span>
  <span class="abs dot" style="left:637px"></span>
</section>

<section>
  <h2 class="abs welcome-title">WEL COME TO PELORIS</h2>
  <p class="abs welcome-text">Lorem ipsum dolor sit amet, consectetur adipiscing elit, sed do eiusmod tempor incididunt ut labore et dolore magna aliqua. Quis ipsum suspendisse ultrices gravida. Risus commodo viverra maecenas accumsan lacus vel facilisis. do eiusmod tempor incididunt ut labore et dolore magna aliqua. Quis ipsum suspendisse ultrices gravida.</p>

  <article class="abs card photo-brick" style="left:0" role="img" aria-label="Brick corner building with arched ground floor">
    <div class="shade">
      <h3>PROPERTY ACQUISITIONS</h3>
      <p>Lorem ipsum dolor sit amet, consectetur adipiscing elit, sed do eiusmod tempor incididunt ut labore et dolore magna aliqua Quis ipsum suspendisse ultrices gravida.</p>
      <a class="btn-more" style="left:442px;top:97px">See more <svg width="22" height="8" viewBox="0 0 22 8"><path d="M0 4h20M16 1l4 3-4 3" stroke="#fff" stroke-width="1.5" fill="none"/></svg></a>
    </div>
  </article>
  <article class="abs card photo-white" style="left:612px" role="img" aria-label="White modern development with arched colonnade and trees">
    <div class="shade">
      <h3>PROPERTY DEVELOPMENT</h3>
      <p>Lorem ipsum dolor sit amet, consectetur adipiscing elit, sed do eiusmod tempor incididunt ut labore et dolore magna aliqua Quis ipsum suspendisse ultrices gravida.</p>
      <a class="btn-more" style="left:442px;top:97px">See more <svg width="22" height="8" viewBox="0 0 22 8"><path d="M0 4h20M16 1l4 3-4 3" stroke="#fff" stroke-width="1.5" fill="none"/></svg></a>
    </div>
  </article>
</section>

<section>
  <div class="abs stone"></div>
  <div class="abs mgmt-photo photo-tower" role="img" aria-label="Glass office tower beside residential blocks"></div>
  <div class="abs mgmt-box">
    <h3>PROPERTY MANAGEMENT</h3>
    <p>Lorem ipsum dolor sit amet, consectetur adipiscing elit, sed do eiusmod tempor incididunt ut labore et dolore magnuis ipsum suspendisse ultrices gravida.</p>
    <a class="btn-more" style="left:46px;top:184px;width:113px">See more <svg width="22" height="8" viewBox="0 0 22 8"><path d="M0 4h20M16 1l4 3-4 3" stroke="#fff" stroke-width="1.5" fill="none"/></svg></a>
  </div>

  <div class="abs rule" style="left:84px;top:2171px;width:417px"></div>
  <div class="abs rule" style="left:680px;top:2171px;width:435px"></div>
  <h2 class="abs section-title" style="left:501px;top:2155px;width:179px">OUR PROJECTS</h2>
  <span class="abs filter" style="left:466px;font-size:22px;top:2217px">ALL</span>
  <span class="abs filter" style="left:524px;font-size:18px;top:2221px">Recidential</span>
  <span class="abs filter" style="left:638px;font-size:18px;top:2221px">Commercial</span>

  <div class="abs photo-thin-glass" style="left:110px;top:2391px;width:59px;height:210px" role="img" aria-label="Glass tower project"></div>
  <div class="abs photo-thin-brick" style="left:178px;top:2348px;width:122px;height:296px" role="img" aria-label="Brick apartment project"></div>
  <div class="abs photo-campus" style="left:309px;top:2292px;width:582px;height:410px" role="img" aria-label="Glass office campus with lawn and pathway"></div>
  <div class="abs photo-thin-brick" style="left:898px;top:2348px;width:123px;height:296px" role="img" aria-label="Brick building project"></div>
  <div class="abs photo-tower" style="left:1030px;top:2391px;width:59px;height:210px" role="img" aria-label="Glass tower project"></div>
  <svg class="arrow" style="left:22px;top:2472px" width="34" height="52" viewBox="0 0 34 52"><path d="M30 3 6 26l24 23" fill="none" stroke="#fff" stroke-width="7"/><path d="M30 3 6 26l24 23" fill="none" stroke="#333" stroke-width="3"/></svg>
  <svg class="arrow" style="left:1143px;top:2472px" width="34" height="52" viewBox="0 0 34 52"><path d="M4 3l24 23L4 49" fill="none" stroke="#fff" stroke-width="7"/><path d="M4 3l24 23L4 49" fill="none" stroke="#333" stroke-width="3"/></svg>
  <h3 class="abs project-name">PROJECT NAME</h3>
  <p class="abs project-text">Lorem ipsum dolor sit amet, consectetur adipiscing elit, sed do eiusmod tempor incididunt ut labore et dolore magnuis ipsum suspendisse ultrices gravida.</p>
</section>

<section>
  <div class="abs keep"></div>
  <div class="abs rule" style="left:84px;top:2927px;width:401px"></div>
  <div class="abs rule" style="left:712px;top:2927px;width:403px"></div>
  <h2 class="abs section-title" style="left:485px;top:2911px;width:227px">KEEP UP TO DATE</h2>
  <p class="abs keep-sub">Hear more about our latest projects and new opportunities.</p>

  <div class="abs signup photo-dusk" role="img" aria-label="Residential towers at dusk with trees"></div>
  <form class="abs signup-panel"></form>
  <div class="abs field" style="top:3155px">First name <b>*</b></div>
  <div class="abs field" style="top:3199px">Last name <b>*</b></div>
  <div class="abs field" style="top:3243px">Email ID <b>*</b></div>
  <div class="abs field" style="top:3287px">Phone <b>*</b></div>
  <p class="abs interest">I'm interested in</p>
  <span class="abs chip" style="left:90px;width:93px">Latest News</span>
  <span class="abs chip" style="left:198px;width:92px">Investing</span>
  <span class="abs chip" style="left:300px;width:94px">Buying</span>
  <span class="abs chip" style="left:409px;width:93px">Leasing</span>
  <span class="abs submit">SUBMIT</span>
</section>

<footer class="abs footer">
  <nav class="footer-nav">
    <a>Home</a><span class="sep">|</span><a>Property</a><span class="sep">|</span><a>Capital and Finance</a><span class="sep">|</span><a>About</a><span class="sep">|</span><a>Contact</a>
  </nav>
  <p class="copy">©2019 Peloris. All rights reserved. • Terms &amp; Conditions • Privacy Policy</p>
</footer>

</body>
</html>
```